Modernes Karten-Design für Finanzdienstleister
Zielgruppe
Wir sind ein Finanzdienstleister, der zum einen Teil auf Provisionsbasis und zum anderen Teil auf Honorarbasis arbeitet. Hierfür haben wir auch getrennte Firmenbereiche. Unser Kundenklientel sind Privatpersonen im Alter zwischen 35 und 80 Jahren. Unsere Dienstleistungen drehen sich um alle Versicherungen, aber auch um Geldanlagen, Verfügungen, Vollmachten und Testamente
Aufgabenstellung
Wir benötigen eine Karte, die wir an Kunden verschicken, wenn wir Unterlagen verschicken. Die Karte, die wir bisher haben finden Sie bei den Dateien, die wir hochgeladen haben. Wir möchten nun eine moderne Karte haben mit der wir uns bei unseren Kunden bedanken. Auf der Rückseite der Karte soll wie bisher Platz sein für einen handschriftlichen Gruß von uns oder für sonstige handschriftliche Vermerke. Beim Format der Karte sind wir fexibel. Es müssen unsere Firmenfarben und unser Slogan verwendet werden. Wir möchten ein schnörkelloses modernes Design haben. Bei den hochgeladenen Unterlagen befinden sich auch Vorschläge, die ein Mitarbeiter bereits entworfen hat. Diese gefallen uns aber nicht. Die Webadresse unserer Webseite lautet: https://lindqvist-lebenswege.example/
Auf der Rückseite sollen natürlich auch die Adress- und Kontaktdaten mit drauf sein. Wir brauchen hier keine eigenen Bilder und auch kein Stockmaterial. Die Karte soll einfach, schlicht aber stylisch modern sein.

```html
<!DOCTYPE html>
<html lang="de">
<head>
<meta charset="utf-8">
<title>Dankeskarte – Lindqvist Lebenswege</title>
<link rel="stylesheet" href="https://fonts.googleapis.com/css2?family=Oswald:wght@300;400;500&display=swap">
<style>
  :root {
    --page-bg: #e7e7e7;
    --card-bg: #f3f3f3;
    --brand-orange: #e4700c;
    --soft-grey: #d4d4d4;
    --quote-grey: #cdcdcd;
    --headline-grey: #666666;
    --text-dark: #2f2f2f;
  }
  * { margin: 0; padding: 0; box-sizing: border-box; }
  html, body {
    width: 1200px; height: 800px; overflow: hidden;
    background: var(--page-bg);
    font-family: "Oswald", sans-serif;
  }
  .stage { position: relative; width: 1200px; height: 800px; }
  .card {
    position: absolute; top: 238px;
    width: 455px; height: 323px;
    background: var(--card-bg);
    overflow: hidden;
  }
  .card--front { left: 114px; }
  .card--back { left: 627px; }
  .card svg.decor { position: absolute; inset: 0; }
  .headline {
    position: absolute; left: 88px; top: 131px;
    font-size: 62px; font-weight: 500; line-height: 1;
    letter-spacing: -0.4px;
    color: var(--headline-grey);
    white-space: nowrap;
  }
  .brand {
    position: absolute; left: 45px; top: 34px;
  }
  .brand__name {
    font-size: 19px; font-weight: 400; line-height: 1;
    color: var(--text-dark); letter-spacing: 0.2px;
    display: flex; align-items: center; gap: 6px;
    white-space: nowrap;
  }
  .brand__dot {
    width: 6px; height: 6px; border-radius: 50%;
    background: var(--brand-orange); display: inline-block;
  }
  .brand__slogan {
    margin-top: 4px; margin-left: 38px;
    font-size: 9px; font-weight: 400;
    color: var(--text-dark); letter-spacing: 0.3px;
    white-space: nowrap;
  }
  .contact {
    position: absolute; left: 293px; top: 222px;
    font-size: 12px; font-weight: 300; line-height: 15.7px;
    color: var(--text-dark); font-style: normal;
    white-space: nowrap;
  }
</style>
</head>
<body>
<main class="stage">

  <section class="card card--front" aria-label="Vorderseite">
    <svg class="decor" width="455" height="323" viewBox="0 0 455 323">
      <circle cx="10" cy="37" r="75" fill="var(--soft-grey)"/>
      <circle cx="385" cy="57" r="12.6" fill="var(--soft-grey)"/>
      <circle cx="64" cy="258" r="12.6" fill="var(--brand-orange)"/>
      <circle cx="456" cy="284" r="84" fill="var(--brand-orange)"/>
      <g class="quote-open" fill="var(--brand-orange)" transform="translate(50 44)">
        <path d="M0,47 V22 C0,8 8,0 22,0 H26 V10 H22 C16,10 13,14 13,20 H26 V47 Z"/>
        <path transform="translate(35 0)" d="M0,47 V22 C0,8 8,0 22,0 H26 V10 H22 C16,10 13,14 13,20 H26 V47 Z"/>
      </g>
      <g class="quote-close" fill="var(--quote-grey)" transform="translate(403 275) rotate(180)">
        <path d="M0,47 V22 C0,8 8,0 22,0 H26 V10 H22 C16,10 13,14 13,20 H26 V47 Z"/>
        <path transform="translate(34 0)" d="M0,47 V22 C0,8 8,0 22,0 H26 V10 H22 C16,10 13,14 13,20 H26 V47 Z"/>
      </g>
    </svg>
    <h1 class="headline">Dankeschön</h1>
  </section>

  <section class="card card--back" aria-label="Rückseite">
    <svg class="decor" width="455" height="323" viewBox="0 0 455 323">
      <circle cx="-9" cy="278" r="80" fill="var(--brand-orange)"/>
    </svg>
    <div class="brand">
      <div class="brand__name"><span class="brand__dot"></span>lindqvist lebenswege</div>
      <div class="brand__slogan">Wege klug begleiten.</div>
    </div>
    <address class="contact">
      Hollerweg 12<br>
      79100 Talheim<br>
      Tel.Nr.: 0761/00 00 12-34<br>
      info@lindqvist-lebenswege.example<br>
      www.lindqvist-lebenswege.example
    </address>
  </section>

</main>
</body>
</html>
```